Business Card

I need a business card that is fresh, styling and reflects my heart centered healing business while still maintaining full professionalism as I have an my evidence-based practice. I am a Naturopath and a Shiatsu Massage Therapist.
Below are my existing logo (file 1) and an inspiration image (file 2) that reflects the colours and style I would like to express to my card (blues greens). I especially like that tree wallpaper.

Information for the card:
Maren Throsby
BHSc. (Nat) m.ROSC
Naturopath
Herbalist
Nutritionist
Shiatsu Therapist
Wellness Counsellor

47 Dunmore St South Fremantle
www.marenthrosby-demo.com.au
maren@marenthrosby-demo.com.au

NOte: I've removed part of the brief, in that I've changed my mind about the back of the card being a '5 treatments and get sixth one free" I'd rather have this on a separate card. So please do not include this in your designs.

Hi Guys, I've taken the '5 session get the sixth free' part out of the brief. Also, I've added the info to go on the business card into the brief.

Thanks and happy designing
Mar

I've just uploaded a high res better quality version of the hand logo. Thanks Lovlies. 

Target Market(s)

I am targeting western women of ages 25 - 40 in preconception care, sugar addiction therapy, and wellness coaching. I want must card to be vibrant, positive and current.

Industry/Entity Type

Business

Requirements
Must have
• Please include my hand image logo

```html
<!DOCTYPE html>
<html lang="en">
<head>
<meta charset="utf-8">
<title>Maren Throsby – Business Card</title>
<link rel="stylesheet" href="https://fonts.googleapis.com/css2?family=Cinzel:wght@700;900&family=Marcellus&display=swap">
<style>
  :root {
    --forest-deep: #021404;
    --forest-dark: #083a0d;
    --forest-mid: #178a1d;
    --forest-bright: #46e03c;
    --sky: #f6f9f4;
    --title-red: #ee2418;
    --title-shadow: rgba(25, 0, 0, 0.9);
    --contact-white: #ffffff;
  }
  html, body {
    margin: 0;
    padding: 0;
    width: 1200px;
    height: 741px;
    overflow: hidden;
    background: #ffffff;
  }
  .card {
    position: relative;
    width: 1200px;
    height: 741px;
    overflow: hidden;
  }
  .card__rainforest {
    position: absolute;
    inset: 0;
    background:
      radial-gradient(ellipse 200px 110px at 930px 50px, var(--sky) 0%, rgba(246,249,244,0.55) 50%, rgba(246,249,244,0) 100%),
      radial-gradient(ellipse 320px 260px at 800px 300px, var(--forest-bright) 0%, rgba(70,224,60,0) 100%),
      radial-gradient(ellipse 240px 200px at 1090px 420px, rgba(70,224,60,0.7) 0%, rgba(70,224,60,0) 100%),
      radial-gradient(ellipse 320px 150px at 600px 720px, rgba(110,230,80,0.7) 0%, rgba(110,230,80,0) 100%),
      radial-gradient(ellipse 200px 300px at 1180px 600px, rgba(2,20,4,0.8) 0%, rgba(2,20,4,0) 100%),
      radial-gradient(ellipse 420px 380px at 180px 380px, var(--forest-dark) 0%, rgba(8,58,13,0) 100%),
      linear-gradient(180deg, var(--forest-dark) 0%, var(--forest-mid) 45%, var(--forest-dark) 80%, var(--forest-deep) 100%);
  }
  .card__name,
  .card__credentials {
    font-family: "Cinzel", serif;
    font-weight: 900;
    color: var(--title-red);
    text-shadow: 2px 2px 2px var(--title-shadow), 0 0 5px rgba(0,0,0,0.6);
    white-space: nowrap;
    margin: 0;
  }
  .card__name {
    position: absolute;
    left: 72px;
    top: 72px;
    font-size: 72px;
    line-height: 1;
  }
  .card__credentials {
    position: absolute;
    left: 72px;
    top: 143px;
    padding: 0;
    list-style: none;
    font-size: 48px;
    line-height: 59.5px;
  }
  .card__contact {
    position: absolute;
    left: 454px;
    top: 524px;
    margin: 0;
    font-family: "Marcellus", serif;
    font-style: normal;
    font-size: 42px;
    line-height: 59px;
    color: var(--contact-white);
    text-shadow: 1px 1px 2px rgba(0,0,0,0.6);
    white-space: nowrap;
  }
  .card__contact span { display: block; }
</style>
</head>
<body>
  <main class="card">
    <div class="card__rainforest" role="img" aria-label="Full-bleed photograph of a lush green rainforest with palms and ferns, bright sky glimpsed at top right"></div>
    <h1 class="card__name">Maren Throsby</h1>
    <ul class="card__credentials">
      <li>BHSc. (Nat) m.ROSC</li>
      <li>Naturopath</li>
      <li>Herbalist</li>
      <li>Nutritionist</li>
      <li>Shiatsu Therapist</li>
      <li>Wellness Counsellor</li>
    </ul>
    <address class="card__contact">
      <span>47 Dunmore St South Fremantle</span>
      <span>www.marenthrosby-demo.com.au</span>
      <span>maren@marenthrosby-demo.com.au</span>
    </address>
  </main>
</body>
</html>
```